Corrindale Planners, LLC Stationary

Corrindale Planners, LLC is a new financial planning and consulting company. We are looking for designs on business cards, letterhead, envelopes, and anything else that would be useful. Our preference for business card design is two sided. We are looking for a professional and clean look with incorporating the logo and patriotic feel. Thank you to all who participate and good luck!

```html
<!DOCTYPE html>
<html lang="en">
<head>
<meta charset="UTF-8">
<title>Corrindale Planners, LLC – Business Card</title>
<link href="https://fonts.googleapis.com/css2?family=Michroma&family=Play:wght@400;700&display=swap" rel="stylesheet">
<style>
  :root {
    --backdrop: #d8d3cc;
    --card-light: #eceef1;
    --card-light-edge: #dfe2e7;
    --navy: #1d2b49;
    --navy-deep: #0f1930;
    --brand-red: #b3202a;
    --silver: #c9cdd3;
    --ink: #2a2c31;
    --ink-soft: #3c3f46;
  }
  * { margin: 0; padding: 0; box-sizing: border-box; }
  html, body {
    width: 1200px; height: 969px; overflow: hidden;
    background: var(--backdrop);
  }
  .canvas {
    position: relative; width: 1200px; height: 969px;
  }
  .business-card {
    position: absolute; left: 100px; top: 201px;
    width: 1000px; height: 566px;
    background: linear-gradient(135deg, var(--card-light) 0%, var(--card-light-edge) 100%);
    box-shadow: 0 18px 40px rgba(0,0,0,0.22);
    overflow: hidden;
    font-family: "Play", sans-serif;
    color: var(--ink);
  }
  .navy-panel {
    position: absolute; inset: 0;
    background: linear-gradient(160deg, var(--navy) 0%, var(--navy-deep) 100%);
    clip-path: polygon(487px 0, 100% 0, 100% 100%, 714px 100%);
  }
  .brand {
    position: absolute; left: 43px; top: 128px;
    display: flex; align-items: center; gap: 12px;
  }
  .brand-dot {
    width: 30px; height: 30px; border-radius: 50%;
    background: var(--brand-red);
  }
  .brand-name {
    font-family: "Play", sans-serif;
    font-weight: 700; font-size: 30px;
    color: var(--navy); letter-spacing: 0.3px;
    white-space: nowrap;
  }
  .person {
    position: absolute; left: 610px; top: 62px; width: 380px;
    text-align: center; color: var(--silver);
  }
  .person-name {
    font-family: "Michroma", sans-serif;
    font-size: 28px; letter-spacing: 1px; line-height: 1.2;
    white-space: nowrap;
  }
  .person-title {
    font-family: "Play", sans-serif;
    font-size: 26px; letter-spacing: 2px; margin-top: 4px;
  }
  .address {
    position: absolute; left: 43px; top: 282px;
    font-size: 26px; line-height: 34px; color: var(--ink-soft);
  }
  .contact-list {
    position: absolute; left: 43px; top: 376px;
    list-style: none;
  }
  .contact-list li {
    display: flex; align-items: center; gap: 14px;
    height: 38.5px; font-size: 24px; color: var(--ink-soft);
  }
  .contact-list svg { width: 24px; height: 24px; fill: var(--ink); flex: none; }
</style>
</head>
<body>
<div class="canvas">
  <div class="business-card">
    <div class="navy-panel"></div>

    <div class="brand">
      <span class="brand-dot"></span>
      <span class="brand-name">Corrindale Planners, LLC</span>
    </div>

    <div class="person">
      <div class="person-name">EVAN PARKS</div>
      <div class="person-title">CEO/FOUNDER</div>
    </div>

    <div class="address">
      <div>4126 Birchwood Court</div>
      <div>Juneau, Alaska 34518</div>
    </div>

    <ul class="contact-list">
      <li>
        <svg viewBox="0 0 24 24" aria-hidden="true"><path d="M6.6 10.8a15.1 15.1 0 0 0 6.6 6.6l2.2-2.2c.3-.3.7-.4 1-.2 1.1.4 2.3.6 3.6.6.6 0 1 .4 1 1V20c0 .6-.4 1-1 1A17 17 0 0 1 3 4c0-.6.4-1 1-1h3.5c.6 0 1 .4 1 1 0 1.3.2 2.5.6 3.600.1.3 0 .7-.2 1z"/></svg>
        <span>512 806 3174</span>
      </li>
      <li>
        <svg viewBox="0 0 24 24" aria-hidden="true"><path d="M6 3h12v5H6zM4 9h16c1.1 0 2 .9 2 2v6h-4v4H6v-4H2v-6c0-1.1.9-2 2-2zm4 7v3h8v-3z"/></svg>
        <span>512 806 3175</span>
      </li>
      <li>
        <svg viewBox="0 0 24 24" aria-hidden="true"><path d="M3 5h18c.6 0 1 .4 1 1v12c0 .6-.4 1-1 1H3c-.6 0-1-.4-1-1V6c0-.6.4-1 1-1zm1 2.2V17h16V7.2l-8 5.3z M4.5 7 12 12 19.5 7z"/></svg>
        <span>hello@corrindale.com</span>
      </li>
      <li>
        <svg viewBox="0 0 24 24" aria-hidden="true"><path d="M12 2a10 10 0 1 0 0 20 10 10 0 0 0 0-20zm-1 17.9A8 8 0 0 1 4.2 10.6L9 15.4v1c0 1.1.9 2 2 2zm6.9-2.6c-.3-.8-1-1.3-1.9-1.3h-1v-3c0-.6-.4-1-1-1H8v-2h2c.6 0 1-.4 1-1V7h2c1.1 0 2-.9 2-2v-.4a8 8 0 0 1 2.9 12.7z"/></svg>
        <span>www.corrindale.com</span>
      </li>
    </ul>
  </div>
</div>
</body>
</html>
```